A Better Way to Celebrate

Bramblecast is a party invitation service with a charity twist. Users can send party invitations to guests, giving them the option to contribute money instead of bring a gift. All money contributed is pooled and split between getting a special present from all, and giving to a local charity.

Bramblecast tagline is “One for you, one for charity”

The target audience are people involved in: kids birthdays, farewell/leaving parties, baby showers, adult birthday parties, teacher gifts,

- an easy way to give to charity
- get the gift you really want. And get less gifts, so no issues with trying to store things you don’t need or won’t get played with
- eco friendly, reduces the need for paper. Less gifts mean less garbage to be thrown away
- saves guests the hassle of shopping, saves time
- easy way to manage your party. The Host Panel tracks all RSVPs, contributions and can send thank you cards (similar to okura and lanternwick).

We would like to have a catchy, exciting fun yet elegant double sided flyer with emphasis on clear communication of the Bramblecas concept (get the gift you really want, give some back to a local charity) and the above listed benefits.

The front page should ideally have one or a few inspirational images and the back side should be more descriptional. Please visit our website: bramblecast-invites.example for more details.

It should fit half an A4 page.

Reason: We still haven't decided on the final design.

Target Market(s)

Children, Adults (farewell parties, anniversaries, birthdays, baby showers)

Our website is mainly kids oriented at the moment but we would like to include the above target audience as well.

Industry/Entity Type

Communication

Requirements
Must have
• Get one big gift you really want (instead of piles of un-needed gifts) and give some back to charity.

Must show that Bramblecast can be a great tool for managing the invitation process (sending the online invitations, tracking the rsvps, sending reminders and thank you mails as well as tracking payments for a pooled gift. (ie. knowing who contributed online to a pooled gift, so no more hassle of reminding people to bring money and manually track who contributed and who didn't)

```html
<!DOCTYPE html>
<html lang="en">
<head>
<meta charset="utf-8">
<title>Bramblecast – Front of Flyer</title>
<link rel="stylesheet" href="https://fonts.googleapis.com/css2?family=Anton&family=Arimo:ital,wght@0,400;1,700&family=Great+Vibes&display=swap">
<style>
  :root {
    --backdrop: #262c30;
    --paper: #ffffff;
    --red-deep: #6e1518;
    --red-mid: #b01a22;
    --red-bright: #d8232c;
    --cyan: #3fc3ee;
    --gold: #ffb21a;
    --gold-light: #ffd04a;
    --maroon: #8a1a22;
    --ink: #222222;
    --ink-soft: #4a4a4a;
    --accent-pink: #e0357a;
    --photo-warm: #f6c77a;
    --photo-cool: #7fa6d8;
  }
  * { box-sizing: border-box; margin: 0; padding: 0; }
  html, body {
    width: 1027px;
    height: 1200px;
    overflow: hidden;
    background: var(--backdrop);
  }
  .flyer {
    position: absolute;
    left: 203px;
    top: 230px;
    width: 650px;
    height: 838px;
    background: var(--paper);
    overflow: hidden;
  }
  .flyer__header {
    position: absolute;
    inset: 0;
    width: 650px;
    height: 838px;
  }
  .headline__kicker {
    position: absolute;
    left: 206px;
    top: 36px;
    font-family: "Arimo", Arial, sans-serif;
    font-style: italic;
    font-weight: 700;
    font-size: 31px;
    color: #fff;
    white-space: nowrap;
  }
  .headline__numeral {
    position: absolute;
    left: 88px;
    top: 40px;
  }
  .headline__line {
    position: absolute;
    left: 202px;
    font-family: "Anton", Impact, sans-serif;
    font-size: 90px;
    line-height: 1;
    color: #fff;
    white-space: nowrap;
    letter-spacing: 0.5px;
  }
  .headline__line--you { top: 72px; }
  .headline__line--charity { top: 180px; }
  .headline__you { color: var(--cyan); }
  .headline__charity {
    background: linear-gradient(180deg, var(--gold-light), var(--gold) 55%, #f59a10);
    -webkit-background-clip: text;
    background-clip: text;
    color: transparent;
  }
  .headline__script {
    position: absolute;
    left: 66px;
    top: 276px;
    font-family: "Great Vibes", cursive;
    font-size: 46px;
    color: #fff;
    white-space: nowrap;
    text-shadow: 0 0 8px rgba(255, 220, 200, 0.9), 0 0 2px #fff;
  }
  .flyer__photo {
    position: absolute;
    left: 252px;
    top: 420px;
    width: 398px;
    height: 418px;
    background:
      radial-gradient(ellipse 55% 35% at 50% 28%, var(--photo-warm), rgba(246,199,122,0) 70%),
      radial-gradient(ellipse 40% 25% at 70% 25%, var(--photo-cool), rgba(127,166,216,0) 70%),
      radial-gradient(ellipse 50% 30% at 55% 80%, #ecd6c6, rgba(236,214,198,0) 75%);
  }
  .brand {
    position: absolute;
    left: 37px;
    top: 579px;
  }
  .brand__plate {
    width: 277px;
    height: 69px;
    background: #f3f3f3;
    display: flex;
    align-items: center;
    gap: 12px;
    padding-left: 14px;
  }
  .brand__mark {
    width: 26px;
    height: 26px;
    background: var(--accent-pink);
  }
  .brand__name {
    font-family: "Arimo", Arial, sans-serif;
    font-size: 31px;
    color: var(--ink-soft);
  }
  .brand__tagline {
    margin-top: 7px;
    padding-left: 30px;
    font-family: "Arimo", Arial, sans-serif;
    font-size: 17px;
    color: var(--ink);
  }
  .brand__url {
    margin-top: 6px;
    padding-left: 30px;
    font-family: "Arimo", Arial, sans-serif;
    font-size: 18px;
    color: var(--cyan);
  }
</style>
</head>
<body>
  <main class="flyer">
    <svg class="flyer__header" viewBox="0 0 650 838" aria-hidden="true">
      <defs>
        <linearGradient id="red-field" x1="0" y1="0" x2="0" y2="1">
          <stop offset="0" stop-color="var(--red-deep)"/>
          <stop offset="0.55" stop-color="var(--red-mid)"/>
          <stop offset="1" stop-color="var(--red-bright)"/>
        </linearGradient>
      </defs>
      <path d="M0 0 H650 V325 C560 345 500 360 430 395 C330 440 200 460 0 482 Z" fill="url(#red-field)"/>
      <path d="M0 242 C200 200 420 165 650 138 L650 146 C420 174 200 210 0 254 Z" fill="#ffffff" opacity="0.45"/>
      <path d="M0 264 C220 216 430 180 650 156 L650 161 C430 186 220 224 0 272 Z" fill="#ffffff" opacity="0.35"/>
      <path d="M0 282 C230 232 440 196 650 172 L650 175 C440 200 240 238 0 288 Z" fill="#ffffff" opacity="0.3"/>
    </svg>

    <p class="headline__kicker">A Better Way to Celebrate</p>

    <svg class="headline__numeral" width="115" height="225" viewBox="0 0 115 225" aria-label="1">
      <defs>
        <linearGradient id="numeral-fill" x1="0" y1="0" x2="0" y2="1">
          <stop offset="0" stop-color="var(--cyan)"/>
          <stop offset="0.5" stop-color="var(--cyan)"/>
          <stop offset="0.5" stop-color="var(--maroon)"/>
          <stop offset="1" stop-color="var(--maroon)"/>
        </linearGradient>
      </defs>
      <text x="57" y="218" text-anchor="middle" font-family="Anton, Impact, sans-serif" font-size="235"
            fill="url(#numeral-fill)" stroke="#ffd9a0" stroke-width="5" paint-order="stroke">1</text>
    </svg>

    <h1>
      <span class="headline__line headline__line--you">for <span class="headline__you">you,</span></span>
      <span class="headline__line headline__line--charity">for <span class="headline__charity">charity</span></span>
    </h1>

    <p class="headline__script">Get what you want and give a little back</p>

    <div class="flyer__photo" role="img" aria-label="Bunch of colourful balloons rising from a gift box held on an open hand"></div>

    <div class="brand">
      <div class="brand__plate">
        <span class="brand__mark"></span>
        <span class="brand__name">bramblecast</span>
      </div>
      <p class="brand__tagline">one for you, one for charity</p>
      <p class="brand__url">www.bramblecast-invites.example</p>
    </div>
  </main>
</body>
</html>
```